QuillMark Business Cards

I need a business card designed for QuillMark. To get an idea of what we do please visit https://formvault.example/para-creadores-3

```html
<!DOCTYPE html>
<html lang="en">
<head>
<meta charset="utf-8">
<title>QuillMark Business Cards</title>
<link rel="stylesheet" href="https://fonts.googleapis.com/css2?family=Montserrat:wght@400;500;700&family=Raleway:wght@400;500&display=swap">
<style>
  :root {
    --page-bg: #e6e7e9;
    --card-bg: #1b1d22;
    --accent: #e8961e;
    --text-light: #ffffff;
    --rule-light: #d9d9d9;
  }
  * { margin: 0; padding: 0; box-sizing: border-box; }
  html, body { width: 1048px; height: 1200px; overflow: hidden; }
  body {
    background: var(--page-bg);
    position: relative;
    font-family: "Raleway", sans-serif;
    color: var(--text-light);
  }
  .card {
    position: absolute;
    width: 843px;
    height: 482px;
    background: var(--card-bg);
    box-shadow: 0 10px 30px rgba(0,0,0,0.18);
    overflow: hidden;
  }
  .card--front { left: 84px; top: 87px; }
  .card--back { left: 77px; top: 622px; }

  .brand { position: absolute; }
  .brand__dot {
    position: absolute;
    border-radius: 50%;
    border: 3px solid var(--accent);
  }
  .brand__name {
    font-family: "Montserrat", sans-serif;
    font-weight: 400;
    color: var(--text-light);
    white-space: nowrap;
    line-height: 1;
  }
  .brand__tagline {
    display: flex;
    align-items: center;
    font-family: "Montserrat", sans-serif;
    color: var(--accent);
    white-space: nowrap;
    text-transform: uppercase;
  }
  .brand__tagline::after {
    content: "";
    flex: 1;
    height: 1px;
    background: var(--rule-light);
    margin-left: 4px;
  }

  .card--front .brand__dot { left: 58px; top: 91px; width: 60px; height: 60px; }
  .card--front .brand__name {
    position: absolute; left: 179px; top: 94px;
    font-size: 44px; letter-spacing: 0.2em;
  }
  .card--front .brand__tagline {
    position: absolute; left: 179px; top: 138px; width: 326px;
    font-size: 11px; letter-spacing: 0.52em;
  }

  .person {
    position: absolute; right: 49px; top: 264px; text-align: right;
  }
  .person__name {
    font-family: "Montserrat", sans-serif; font-weight: 700;
    font-size: 38px; letter-spacing: -1.5px; color: var(--accent);
    line-height: 1.1;
  }
  .person__role {
    font-family: "Montserrat", sans-serif; font-weight: 400;
    font-size: 22px; margin-top: 4px; letter-spacing: 0.3px;
  }
  .divider {
    position: absolute; left: 48px; right: 49px; top: 344px;
    height: 2px; background: var(--accent);
  }
  .contacts {
    position: absolute; left: 48px; top: 364px; list-style: none;
  }
  .contacts__item {
    display: flex; align-items: center; height: 30px;
    font-size: 22px;
  }
  .contacts__icon { width: 18px; height: 18px; margin-right: 17px; flex: none; }
  .address {
    position: absolute; right: 49px; top: 382px; text-align: right;
    font-family: "Montserrat", sans-serif; font-size: 21px; line-height: 33px;
  }
  .card__band {
    position: absolute; left: 0; right: 0; bottom: 0; height: 10px;
    background: var(--accent);
  }

  .card--back .brand__name {
    position: absolute; left: 298px; top: 346px;
    font-size: 56px; letter-spacing: 0.2em;
  }
  .card--back .brand__tagline {
    position: absolute; left: 300px; top: 412px; width: 450px;
    font-size: 14px; letter-spacing: 0.6em;
  }
</style>
</head>
<body>
  <section class="card card--front" aria-label="Business card front">
    <div class="brand__dot" aria-hidden="true"></div>
    <div class="brand__name">QUILLMARK</div>
    <div class="brand__tagline">Digital Notary</div>

    <div class="person">
      <div class="person__name">DANIEL HARTLEY</div>
      <div class="person__role">Managing Director</div>
    </div>

    <div class="divider"></div>

    <ul class="contacts">
      <li class="contacts__item">
        <svg class="contacts__icon" viewBox="0 0 24 24" aria-hidden="true">
          <path fill="#e8961e" d="M6.6 10.8a15.1 15.1 0 0 0 6.6 6.6l2.2-2.2a1 1 0 0 1 1-.25 11.4 11.4 0 0 0 3.6.57 1 1 0 0 1 1 1V20a1 1 0 0 1-1 1A17 17 0 0 1 3 4a1 1 0 0 1 1-1h3.5a1 1 0 0 1 1 1c0 1.25.2 2.45.57 3.6a1 1 0 0 1-.25 1z"/>
          <path fill="none" stroke="#e8961e" stroke-width="1.8" d="M14 3a7 7 0 0 1 7 7M14 6.5a3.5 3.5 0 0 1 3.5 3.5"/>
        </svg>
        044-123 456 789
      </li>
      <li class="contacts__item">
        <svg class="contacts__icon" viewBox="0 0 24 24" aria-hidden="true">
          <rect x="1" y="4" width="22" height="16" fill="#e8961e"/>
          <path fill="none" stroke="#1b1d22" stroke-width="1.6" d="M1.5 4.5 12 13l10.5-8.5M1.5 19.5l8-7.5M22.5 19.5l-8-7.5"/>
        </svg>
        info@quillmark.example
      </li>
      <li class="contacts__item">
        <svg class="contacts__icon" viewBox="0 0 24 24" aria-hidden="true">
          <circle cx="12" cy="12" r="11" fill="#e8961e"/>
          <path fill="#1b1d22" d="M6 6.5c2 .5 3 1.5 2.5 3s1 2.5 2.5 2.5 1 2.5 0 3.5-.5 3 .5 4.5c-3-.5-5-3-5.5-5S4 11 4 9zM14 3.5c1 1.5 2.5 1.5 3.5 3s-.5 2.5 1 3.5 2 .5 2.5 2c-.5 2-2 3-3 2.5s-2-2-3.5-1.5S13 9 14.5 8 13 5 14 3.5z"/>
        </svg>
        www.quillmark.example
      </li>
    </ul>

    <address class="address" style="font-style: normal;">
      421, Address line here<br>
      Country Name, 45452
    </address>

    <div class="card__band"></div>
  </section>

  <section class="card card--back" aria-label="Business card back">
    <div class="brand__name">QUILLMARK</div>
    <div class="brand__tagline">Digital Notary</div>
  </section>
</body>
</html>
```